Quillo Design Prize - $10,000 tablet app design contest, Event App Category

Quillo is a marketplace for Velo App Templates (similar to PageLoom templates). We want you to design an app template for sale in our marketplace which targets Event Apps (Velo Apps that are created around music festivals, tradeshows, conferences or other events).

It’s up to you to create pages or features for the App Template that you think are appropriate. Creativity will be rewarded! Here are some example pages or features that you could create:

• A welcome page
• Event details – when and where?
• A location map
• A contact details page
• An event calendar (what’s on when?)
• Social media integration
• Video or animations

Your design should be Vibrant, Engaging and Contemporary. If you have an Velo, download Quillo Viewer and download template examples in the download tab.

Your entry must include:
• A brief description of your template
• preview images of all pages of your template

Attached to this project are free templates to help you get started with your design. We have included:
1. A free portfolio template for designers/photographers
2. Icons and artwork to use in your template
3. Blank pages template
4. Form template
5. Video ad template

If you are selected as a finalist you will be required to submit an .oproject file containing:
• Your InDesign source files
• Preview images of your template
• All creative / stock assets used in the template (animations, video etc.)
• A text file with instructions on how to update the template
• A metadata .txt file containing template details and your information

How to enter:
1. Register at Marketplace and view the instructions under the welcome message https://marketplace.quillohub-example.com/welcome
2. Download Quillo Editor: https://support.quillohub-example.com/entries/58174096-quillo-editor
3. Use the free templates provided in this brief to create your designs and submit to Pencilyard

Reason: Due to the Christmas break we are extending the deadline of our competition. Thank you for time and effort - I will be providing feedback over the next couple of days! Best wishes, Loretta

Hi All,

I have received many screenshots with some great designs! I just wanted to clarify that you are designing Quillo app templates including Quillo features and not just page designs?

Read Tips for First Time Quilloers to guide you through the template creation process

Before you start designing templates for Quillo Marketplace

·       Read the Quality Standards

·       Read the Copyright Information 

·       Use the Template Quality Checklist to ensure your template follows our guidelines. 

What should my project file contain?

·       A folder containing your source files, e.g. InDesign. This must be named Source.

·       The Quillo content files. This must be named Bundle.

·       Instructions, explaining to a customer how to use your template.

Best wishes,

Loretta

Reason: We are extending the competition by 7 days to give you more time!

Reason: Hello - we have received 3 entries for this contest so we are extending the deadline by 7 days. Best wishes, Loretta :)

Target Market(s)

Entrepreneurs who wish to create Velo Apps by using our App design templates.

Industry/Entity Type

Events

Requirements
Must have
• You will need Quillo Editor to open the .oproject files attached to this brief. Get it here: https://support.quillohub-example.com/entries/58174096-quillo-editor
Should not have
• Low quality, fuzzy or blurry images
- Any stock images or content which you do not own the rights to
- Any material which could be considered inappropriate or offensive

```html
<!DOCTYPE html>
<html lang="en">
<head>
<meta charset="utf-8">
<title>Event Bubbles – Tablet App Template Screens</title>
<link rel="stylesheet" href="https://fonts.googleapis.com/css2?family=Open+Sans:wght@600;700&display=swap">
<style>
  :root{
    --page:#eeeff1;
    --screen-mid:#ffffff;
    --screen-edge:#d9dadd;
    --ink:#2b2b2e;
    --ink-soft:#77787c;
    --panel:#f3f3f4;
    --panel-edge:#a9aaae;
    --link-edge:#b8b9bd;
    --link-fill:#f5f5f6;
    --green:#5cbb3a;  --green-lt:#a9e27d;  --green-dk:#3f8f24;
    --blue:#2f9fdc;   --blue-lt:#8fd3f5;   --blue-dk:#1a6fae;
    --yellow:#f6c21d; --yellow-lt:#fde98a; --yellow-dk:#e39a10;
    --orange:#f4801f; --orange-lt:#fcc17a; --orange-dk:#d35d12;
    --purple:#6c3d8e; --purple-lt:#b08bce; --purple-dk:#4a2466;
    --teal:#1db39a;   --teal-lt:#7de0cb;   --teal-dk:#0f8a75;
    --pink:#ee3f8f;   --pink-lt:#fb9bc5;   --pink-dk:#c81f6c;
    --red:#e0262b;    --red-lt:#f88a80;    --red-dk:#a81419;
  }
  *{box-sizing:border-box;margin:0;padding:0}
  html,body{width:1200px;height:720px;overflow:hidden;background:var(--page)}
  body{position:relative;font-family:"Open Sans",Arial,sans-serif;color:var(--ink)}

  .screen{
    position:absolute;overflow:hidden;
    background:radial-gradient(ellipse at 50% 45%,var(--screen-mid) 0%,#f2f2f3 45%,var(--screen-edge) 100%);
    box-shadow:0 1px 3px rgba(0,0,0,.18);
  }
  .screen--gallery{left:62px;top:46px;width:483px;height:316px}
  .screen--hub{left:665px;top:46px;width:475px;height:309px}
  .screen--gallery-mono{left:57px;top:443px;width:305px;height:198px}
  .screen--invitees{left:440px;top:441px;width:308px;height:198px}
  .screen--overview{left:829px;top:441px;width:308px;height:198px}

  .note{position:absolute;left:4px;top:6px;font-weight:700;font-size:9.5px;line-height:13px;color:var(--ink)}
  .note--small{font-size:6px;line-height:9px;left:3px;top:3px}

  .bubble{
    position:absolute;
    left:calc(var(--x) - var(--r));top:calc(var(--y) - var(--r));
    width:calc(var(--r) * 2);height:calc(var(--r) * 2);
    border-radius:50%;
    display:flex;align-items:center;justify-content:center;text-align:center;
    color:#fff;font-weight:700;line-height:1.05;
    text-shadow:0 1px 2px rgba(0,0,0,.35);
    background:radial-gradient(circle at 50% 38%,var(--lt) 0%,var(--c) 55%,var(--dk) 100%);
    box-shadow:0 0 0 calc(var(--r) * .06) var(--dk),0 4px 8px rgba(0,0,0,.28);
  }
  .bubble::after{
    content:"";position:absolute;left:18%;top:5%;width:64%;height:38%;border-radius:50%;
    background:linear-gradient(rgba(255,255,255,.7),rgba(255,255,255,0));
  }
  .bubble span{position:relative;z-index:1}
  .bubble--green{--c:var(--green);--lt:var(--green-lt);--dk:var(--green-dk)}
  .bubble--blue{--c:var(--blue);--lt:var(--blue-lt);--dk:var(--blue-dk)}
  .bubble--yellow{--c:var(--yellow);--lt:var(--yellow-lt);--dk:var(--yellow-dk)}
  .bubble--orange{--c:var(--orange);--lt:var(--orange-lt);--dk:var(--orange-dk)}
  .bubble--purple{--c:var(--purple);--lt:var(--purple-lt);--dk:var(--purple-dk)}
  .bubble--teal{--c:var(--teal);--lt:var(--teal-lt);--dk:var(--teal-dk)}
  .bubble--pink{--c:var(--pink);--lt:var(--pink-lt);--dk:var(--pink-dk)}
  .bubble--red{--c:var(--red);--lt:var(--red-lt);--dk:var(--red-dk)}

  .links{position:absolute;inset:0}
  .links .edge{fill:none;stroke:var(--link-edge);stroke-width:17;stroke-linecap:round}
  .links .fill{fill:none;stroke:var(--link-fill);stroke-width:13;stroke-linecap:round}

  .details-panel{
    position:absolute;left:29px;top:37px;width:252px;height:103px;
    background:var(--panel);border:1px solid var(--panel-edge);border-radius:5px;
    box-shadow:0 2px 4px rgba(0,0,0,.25);
  }
  .details-panel p{position:absolute;left:10px;top:15px;font-size:7.5px;font-weight:700;color:var(--ink-soft)}
</style>
</head>
<body>

<section class="screen screen--gallery" aria-label="Event gallery">
  <p class="note">These bubbles should be moving like air bubbles if possible<br>Larger bubbles are for more important events</p>
  <div class="bubble bubble--green" style="--x:107px;--y:123px;--r:57px;font-size:19px"><span>My New<br>Event</span></div>
  <div class="bubble bubble--blue" style="--x:234px;--y:118px;--r:57px;font-size:19px"><span>My New<br>Event</span></div>
  <div class="bubble bubble--yellow" style="--x:357px;--y:98px;--r:57px;font-size:19px"><span>My New<br>Event</span></div>
  <div class="bubble bubble--orange" style="--x:94px;--y:244px;--r:57px;font-size:19px"><span>My New<br>Event</span></div>
  <div class="bubble bubble--purple" style="--x:220px;--y:228px;--r:33px;font-size:11px"><span>My New<br>Event</span></div>
  <div class="bubble bubble--teal" style="--x:301px;--y:257px;--r:33px;font-size:11px"><span>My New<br>Event</span></div>
  <div class="bubble bubble--pink" style="--x:422px;--y:214px;--r:57px;font-size:19px"><span>My New<br>Event</span></div>
</section>

<section class="screen screen--hub" aria-label="Event hub">
  <svg class="links" viewBox="0 0 475 309" aria-hidden="true">
    <g class="edge">
      <path d="M241 177 C185 150 140 95 57 76"/>
      <path d="M241 177 C290 150 300 100 339 80"/>
      <path d="M241 177 C190 205 160 240 119 250"/>
      <path d="M241 177 C320 185 350 250 420 249"/>
    </g>
    <g class="fill">
      <path d="M241 177 C185 150 140 95 57 76"/>
      <path d="M241 177 C290 150 300 100 339 80"/>
      <path d="M241 177 C190 205 160 240 119 250"/>
      <path d="M241 177 C320 185 350 250 420 249"/>
    </g>
  </svg>
  <div class="bubble bubble--blue" style="--x:241px;--y:177px;--r:61px;font-size:20px"><span>My New<br>Event</span></div>
  <div class="bubble bubble--green" style="--x:57px;--y:76px;--r:40px;font-size:14px"><span>Overview</span></div>
  <div class="bubble bubble--yellow" style="--x:339px;--y:80px;--r:40px;font-size:14px"><span>Invitees</span></div>
  <div class="bubble bubble--teal" style="--x:119px;--y:250px;--r:40px;font-size:14px"><span>Specials</span></div>
  <div class="bubble bubble--red" style="--x:420px;--y:249px;--r:40px;font-size:14px"><span>More</span></div>
</section>

<section class="screen screen--gallery-mono" aria-label="Event gallery, single colour">
  <p class="note note--small">These bubbles should be moving like air bubbles if possible<br>These bubbles should be moving like air bubbles if possible</p>
  <div class="bubble bubble--blue" style="--x:69px;--y:76px;--r:36px;font-size:12px"><span>My New<br>Event</span></div>
  <div class="bubble bubble--blue" style="--x:148px;--y:74px;--r:36px;font-size:12px"><span>My New<br>Event</span></div>
  <div class="bubble bubble--blue" style="--x:226px;--y:60px;--r:36px;font-size:12px"><span>My New<br>Event</span></div>
  <div class="bubble bubble--blue" style="--x:61px;--y:154px;--r:36px;font-size:12px"><span>My New<br>Event</span></div>
  <div class="bubble bubble--blue" style="--x:141px;--y:143px;--r:21px;font-size:7px"><span>My New<br>Event</span></div>
  <div class="bubble bubble--blue" style="--x:191px;--y:161px;--r:21px;font-size:7px"><span>My New<br>Event</span></div>
  <div class="bubble bubble--blue" style="--x:267px;--y:133px;--r:36px;font-size:12px"><span>My New<br>Event</span></div>
</section>

<section class="screen screen--invitees" aria-label="Invitees page">
  <div class="details-panel"><p>Add details about invitees here</p></div>
  <div class="bubble bubble--yellow" style="--x:266px;--y:40px;--r:37px;font-size:12.5px"><span>Invitees</span></div>
  <div class="bubble bubble--teal" style="--x:31px;--y:170px;--r:24px;font-size:8.5px"><span>Specials</span></div>
  <div class="bubble bubble--green" style="--x:81px;--y:168px;--r:24px;font-size:8.5px"><span>Overview</span></div>
  <div class="bubble bubble--red" style="--x:135px;--y:168px;--r:24px;font-size:8.5px"><span>More</span></div>
</section>

<section class="screen screen--overview" aria-label="Overview page">
  <div class="details-panel"><p>Add details about the event here</p></div>
  <div class="bubble bubble--green" style="--x:274px;--y:36px;--r:32px;font-size:11px"><span>Overview</span></div>
  <div class="bubble bubble--teal" style="--x:31px;--y:171px;--r:24px;font-size:8.5px"><span>Specials</span></div>
  <div class="bubble bubble--yellow" style="--x:82px;--y:166px;--r:24px;font-size:8.5px"><span>Invitees</span></div>
  <div class="bubble bubble--red" style="--x:135px;--y:168px;--r:24px;font-size:8.5px"><span>More</span></div>
</section>

</body>
</html>
```